MEN'S WEAR PACKAGING BOX FOR THE YOUTH

We need designs for shirt box packaging.We are into manufacturing of garments and our brand sells mens wear (Formal Shirts).Our shirts are sold in single pcs box.
The following are the requirements :-
1.Box for premium category formal wear (Brand "Vorlane").
A. I would need the design to be very contemporary and clean.
B. Its a formal wear brand so the designs need to be more classy and fresh as the end user are Office goers and young stylish businessmen.
I would need a whole package ie: shirt box,tags and woven shirt label design.If you need any more information then please be free to mail me back and i will be happy to reply.I am attaching my current box design for your reference and also the AI file of the logo and brands.
Updates

Project Deadline Extended Reason: Earlier i had opted for refundable project but now i have changed it to committed package. Added Tuesday, July 28, 2015

Industry/Entity Type

Clothing

Requirements
Must have
• Brand logo / name
• Box size SIZE 60MM X 250MM X 368MM
• The branding layout should not be same as the current design.

```html
<!DOCTYPE html>
<html lang="en">
<head>
<meta charset="UTF-8">
<title>Vorlane Premium — Shirt Box Range</title>
<link rel="stylesheet" href="https://fonts.googleapis.com/css2?family=Raleway:wght@300;400&display=swap">
<style>
  :root {
    --page-bg: #ffffff;
    --deep-teal: #0f4b63;
    --deep-teal-light: #1a6580;
    --deep-teal-dark: #0b3f55;
    --indigo: #352b7a;
    --indigo-light: #463b98;
    --indigo-dark: #2b2266;
    --amber: #f49f22;
    --amber-light: #fbb646;
    --amber-dark: #ee9419;
    --aqua-top: #13a3a6;
    --aqua-bottom: #2fcdc5;
    --aqua-light: #3fd6cd;
    --band-teal: #134d66;
    --mark-light: #e3e7ea;
    --mark-white: #ffffff;
  }
  * { box-sizing: border-box; margin: 0; padding: 0; }
  html, body {
    width: 898px;
    height: 1200px;
    overflow: hidden;
    background: var(--page-bg);
  }
  .box-range {
    position: relative;
    width: 898px;
    height: 1200px;
  }
  .box-cover {
    position: absolute;
    width: 410px;
    height: 575px;
    overflow: hidden;
  }
  .box-cover--maze { left: 27px; top: 12px; }
  .box-cover--leaf { left: 461px; top: 12px; }
  .box-cover--amber { left: 27px; top: 613px; }
  .box-cover--aqua { left: 461px; top: 613px; }

  .pattern-area { position: absolute; inset: 0; }
  .box-cover--maze .pattern-area {
    background:
      radial-gradient(ellipse 60% 40% at 25% 70%, var(--deep-teal-light), transparent 70%),
      radial-gradient(ellipse 50% 35% at 80% 30%, var(--deep-teal-light), transparent 70%),
      linear-gradient(160deg, var(--deep-teal), var(--deep-teal-dark));
  }
  .box-cover--leaf .pattern-area {
    background:
      radial-gradient(ellipse 55% 40% at 70% 60%, var(--indigo-light), transparent 70%),
      radial-gradient(ellipse 50% 35% at 20% 25%, var(--indigo-light), transparent 70%),
      linear-gradient(160deg, var(--indigo), var(--indigo-dark));
  }
  .box-cover--amber .pattern-area {
    background:
      radial-gradient(circle at 50% 30%, var(--amber-light), transparent 45%),
      radial-gradient(circle at 50% 80%, var(--amber-light), transparent 40%),
      linear-gradient(180deg, var(--amber), var(--amber-dark));
  }
  .box-cover--aqua .pattern-area {
    background:
      radial-gradient(ellipse 60% 45% at 65% 35%, var(--aqua-light), transparent 70%),
      linear-gradient(175deg, var(--aqua-top), var(--aqua-bottom));
  }

  .brand-mark {
    position: absolute;
    font-family: "Raleway", sans-serif;
    color: var(--mark-light);
    text-align: center;
    line-height: 1;
  }
  .brand-mark__name {
    display: block;
    font-weight: 300;
    font-size: 30px;
    letter-spacing: 1px;
  }
  .brand-mark__tier {
    display: block;
    font-weight: 300;
    font-size: 11px;
    letter-spacing: 5px;
    margin-top: 3px;
    padding-left: 5px;
  }
  .box-cover--maze .brand-mark,
  .box-cover--leaf .brand-mark { right: 22px; top: 92px; }
  .box-cover--aqua .brand-mark { left: 190px; bottom: 48px; }

  .brand-band {
    position: absolute;
    left: 0;
    right: 0;
    top: 252px;
    height: 72px;
    background: var(--band-teal);
  }
  .brand-band .brand-mark {
    left: 0;
    right: 0;
    top: 17px;
    color: var(--mark-white);
  }
  .brand-band .brand-mark__name { font-size: 26px; font-weight: 400; }
  .brand-band .brand-mark__tier { font-size: 10px; letter-spacing: 4px; }
</style>
</head>
<body>
<main class="box-range">

  <section class="box-cover box-cover--maze">
    <div class="pattern-area" role="img" aria-label="Tonal teal geometric line-maze pattern"></div>
    <div class="brand-mark">
      <span class="brand-mark__name">VORLANE</span>
      <span class="brand-mark__tier">PREMIUM</span>
    </div>
  </section>

  <section class="box-cover box-cover--leaf">
    <div class="pattern-area" role="img" aria-label="Tonal indigo overlapping leaf pattern"></div>
    <div class="brand-mark">
      <span class="brand-mark__name">VORLANE</span>
      <span class="brand-mark__tier">PREMIUM</span>
    </div>
  </section>

  <section class="box-cover box-cover--amber">
    <div class="pattern-area" role="img" aria-label="Fine amber concentric fingerprint line pattern"></div>
    <div class="brand-band">
      <div class="brand-mark">
        <span class="brand-mark__name">VORLANE</span>
        <span class="brand-mark__tier">PREMIUM</span>
      </div>
    </div>
  </section>

  <section class="box-cover box-cover--aqua">
    <div class="pattern-area" role="img" aria-label="Subtle aqua triangular line grid pattern"></div>
    <div class="brand-mark">
      <span class="brand-mark__name">VORLANE</span>
      <span class="brand-mark__tier">PREMIUM</span>
    </div>
  </section>

</main>
</body>
</html>
```